Fitness Clothing Apparel Business Card

This project is linked to Fitness Clothing Apparel, KESTRO, Looking for AWESOME Logo Design!!!.

Our company needs a Business Card Design. Please refer to our original project in the link above.

Hi, I'm looking for a professional logo design which will help brand my clothing and nutrition supplement company. The winner of this contest may be hired again in the future to help design some flyers, banners, graphics, etc.

A little background about the company...
KESTRO Fitness is a new fitness clothing and nutrition company based in Southern California... near the mecca of bodybuilding, Harlow Cove! Our company is based around the culture of fitness and bodybuilding. We design clothing that are functional yet appealing for an athletic individual.

What I would like to see on business card...
The card has communicate our brand values. It needs to have attitude yet professionally done. Our brand colors are black, red, and white.

Target Market(s)

Fitness and bodybuilding enthusiasts

Industry/Entity Type

Nutrition

Font styles to use
Serif
Sans Serif
Decorative
Script

Colors

Designer to choose colors to be used in the design.

Requirements
Must have
• our company logo
Nice to have
• red and black, an abstract design of a bull
Should not have
• I'm open to all ideas, appearance is important

```html
<!DOCTYPE html>
<html lang="en">
<head>
<meta charset="utf-8">
<title>KESTRO Fitness Business Card</title>
<link rel="stylesheet" href="https://fonts.googleapis.com/css2?family=EB+Garamond:wght@400;500&display=swap">
<style>
  :root {
    --ink: #000000;
    --paper: #ffffff;
    --stage: #ffffff;
    --flame: #d6101a;
    --flame-deep: #7a0008;
    --text-light: #f4f4f4;
    --text-dark: #1a1a1a;
  }
  * { box-sizing: border-box; margin: 0; padding: 0; }
  html, body {
    width: 1200px; height: 394px; overflow: hidden;
    background: var(--stage);
  }
  .stage {
    position: relative; width: 1200px; height: 394px; overflow: hidden;
    font-family: "EB Garamond", Georgia, serif;
  }
  .strip {
    position: absolute; left: 18px; width: 560px;
    background: var(--ink); border-radius: 3px;
  }
  .strip--top { top: 10px; height: 85px; }
  .strip--middle { top: 128px; height: 130px; }
  .strip--bottom { top: 292px; height: 86px; }

  .smoke {
    position: absolute;
    background:
      radial-gradient(ellipse 55% 40% at 50% 50%, rgba(230,20,30,0.85), rgba(150,0,10,0.35) 60%, transparent 80%);
  }
  .strip--middle .smoke { left: 0; top: 20px; width: 400px; height: 85px; }

  .brand {
    position: absolute; color: var(--text-light);
    font-weight: 400; letter-spacing: 0.22em; text-align: center;
    display: flex; flex-direction: column; align-items: center; gap: 8px;
  }
  .brand__dot {
    width: 34px; height: 34px; border-radius: 50%;
    background: var(--text-light);
  }
  .strip--middle .brand { left: 420px; top: 40px; width: 150px; font-size: 24px; }

  .card {
    position: absolute; left: 640px; top: 12px; width: 560px; height: 358px;
    background: var(--paper);
  }
  .card__face {
    position: absolute; left: 0; top: 0; width: 560px; height: 306px;
    background: var(--ink);
  }
  .card__face .smoke { left: 0; top: 30px; width: 430px; height: 75px; }
  .card__face .brand { left: 430px; top: 42px; width: 130px; font-size: 19px; gap: 6px; }
  .card__face .brand__dot { width: 28px; height: 28px; }

  .person {
    position: absolute; left: 60px; top: 145px; width: 360px;
    text-align: center; color: var(--text-light);
  }
  .person__name { font-size: 42px; font-weight: 400; letter-spacing: 0.02em; line-height: 1; }
  .person__role { margin-top: 26px; font-size: 18px; letter-spacing: 0.28em; }
  .person__contact {
    margin-top: 22px; font-size: 13.5px; display: flex; justify-content: center; gap: 18px;
  }
  .details {
    position: absolute; left: 441px; top: 150px; list-style: none;
    color: var(--text-light); font-size: 9.5px; line-height: 16px;
  }
  .card__footer {
    position: absolute; left: 0; top: 306px; width: 560px; height: 52px;
    display: flex; flex-direction: column; align-items: center; justify-content: center; gap: 3px;
    color: var(--text-dark); font-size: 11px; letter-spacing: 0.22em;
  }
  .card__footer .brand__dot { width: 16px; height: 16px; border-radius: 50%; background: var(--text-dark); }
</style>
</head>
<body>
<main class="stage">
  <section class="strip strip--top" aria-label="Card back, top"></section>

  <section class="strip strip--middle" aria-label="Card back, brand band">
    <div class="smoke" role="img" aria-label="Flowing red smoke ribbon"></div>
    <div class="brand"><span class="brand__dot"></span><span>KESTRO</span></div>
  </section>

  <section class="strip strip--bottom" aria-label="Card back, bottom"></section>

  <article class="card">
    <div class="card__face">
      <div class="smoke" role="img" aria-label="Flowing red smoke ribbon"></div>
      <div class="brand"><span class="brand__dot"></span><span>KESTRO</span></div>

      <div class="person">
        <h1 class="person__name">DORIAN VALE</h1>
        <p class="person__role">MANAGING DIRECTOR</p>
        <p class="person__contact">
          <span>Phone: (310) 555-0142.</span>
          <span>Email: dorian@kestro.com</span>
        </p>
      </div>

      <ul class="details">
        <li>Address 1</li>
        <li>Address 2</li>
        <li>Address 3</li>
        <li>Email :info@kestro.com</li>
        <li>Phone:</li>
        <li>Social:</li>
        <li>www.social/kestro.com</li>
        <li>Feed: @kestro</li>
      </ul>
    </div>

    <footer class="card__footer">
      <span class="brand__dot"></span>
      <span>KESTRO</span>
    </footer>
  </article>
</main>
</body>
</html>
```